Wellness IV Billboard for Naturopathic Physicians.

We need a billboard design done. We have some templates. The client would like three options to choose from. The IV bag is important this is a wellness IV billboard. The fruit needs color added. The client wants it to be obvious this is about getting a wellness IV. Same day appts available. Bright fruit is in the IV is important. You can find out more about the client at www.verdalo.clinic.

Target Market(s)

Missoula Montana

Industry/Entity Type

Health And Wellness

Font styles to use
Serif
Other font styles liked:
• see attached document with approved fonts

Colors

Designer to choose colors to be used in the design.

Requirements
Must have
• IV, logo, Wellness IVs, Same Day Appointments-See the template. Must use the graphic brand guidelines with font. Font used in template is approved to use.
Nice to have
• Must have iv bag filled with fruit and vegetables.
Should not have
• Use the attached template.

```html
<!DOCTYPE html>
<html lang="en">
<head>
<meta charset="utf-8">
<title>IV Therapy Billboard</title>
<link href="https://fonts.googleapis.com/css2?family=Bree+Serif&family=Open+Sans:ital,wght@0,400;0,600;1,300&display=swap" rel="stylesheet">
<style>
  :root {
    --green: #5b7a2c;
    --paper: #ffffff;
    --frame: #9a9a9a;
    --bg: #ffffff;
    --bag-top: #f2f3f1;
    --bag-mid: #f3e7c4;
    --bag-low: #f6c56a;
    --bag-base: #f3a64a;
  }
  html, body {
    margin: 0;
    padding: 0;
    width: 1200px;
    height: 1199px;
    overflow: hidden;
    background: var(--bg);
  }
  .billboard {
    position: absolute;
    left: 40px;
    top: 343px;
    width: 1120px;
    height: 512px;
    background: var(--paper);
    border: 2px solid var(--frame);
    box-sizing: border-box;
    color: var(--green);
  }
  .iv-bag {
    position: absolute;
    left: 13px;
    top: 8px;
    width: 297px;
    height: 494px;
    border-radius: 26px 26px 40px 40px;
    background: linear-gradient(180deg, var(--bag-top) 0%, var(--bag-top) 25%, var(--bag-mid) 50%, var(--bag-low) 78%, var(--bag-base) 100%);
  }
  .headline {
    position: absolute;
    left: 333px;
    top: 21px;
    margin: 0;
    font-family: "Bree Serif", serif;
    font-weight: 400;
    font-size: 110px;
    line-height: 1;
    letter-spacing: 13px;
    white-space: nowrap;
  }
  .tagline {
    position: absolute;
    left: 336px;
    top: 137px;
    margin: 0;
    font-family: "Bree Serif", serif;
    font-size: 38px;
    letter-spacing: 13px;
    line-height: 1;
    white-space: nowrap;
  }
  .same-day {
    position: absolute;
    left: 380px;
    width: 580px;
    top: 237px;
    text-align: center;
    font-family: "Bree Serif", serif;
    font-size: 42px;
    line-height: 1;
    white-space: nowrap;
  }
  .call {
    position: absolute;
    left: 380px;
    width: 580px;
    top: 294px;
    text-align: center;
    font-family: "Open Sans", sans-serif;
    font-size: 48px;
    line-height: 1;
    white-space: nowrap;
  }
  .call .label { font-style: italic; font-weight: 300; }
  .call .number { font-weight: 600; }
  .learn-more {
    position: absolute;
    left: 337px;
    top: 450px;
    font-family: "Open Sans", sans-serif;
    font-style: italic;
    font-weight: 300;
    font-size: 24px;
    line-height: 1;
    white-space: nowrap;
  }
  .learn-more .url {
    font-family: "Bree Serif", serif;
    font-style: normal;
    font-size: 25px;
    letter-spacing: 7px;
    margin-left: 10px;
  }
  .brand {
    position: absolute;
    left: 940px;
    top: 345px;
    width: 150px;
    text-align: center;
    font-family: "Bree Serif", serif;
    font-size: 34px;
    line-height: 1;
  }
  .brand .mark {
    display: block;
    width: 80px;
    height: 80px;
    margin: 0 auto 14px;
    border-radius: 50%;
    background: var(--green);
  }
</style>
</head>
<body>
  <section class="billboard">
    <div class="iv-bag" role="img" aria-label="Clear IV saline bag filled with bright citrus slices, cucumber and fruit"></div>
    <h1 class="headline">IV THERAPY</h1>
    <p class="tagline">WELLNESS FROM WITH IN</p>
    <div class="same-day">SAME DAY APPOINTMENTS</div>
    <div class="call"><span class="label">CALL:</span><span class="number">406.555.0142</span></div>
    <div class="learn-more">LEARN MORE AT:<span class="url">WWW.VERDALO.CLINIC</span></div>
    <div class="brand"><span class="mark"></span>VERDALO</div>
  </section>
</body>
</html>
```